Multi brand diverse distributor requires new business card

We're a distributor representing multiple brands and would like a new business card reflecting our diversity.

We incorporate landscape architecture, environmental engineering and sustainability into construction projects.

KV Holdings is the company name, and therefore the KV logo should be the primary logo.

Target Market(s)

Engineers, Landscape Architects, Environmental

Contact Information for Business Card

See sample

Colors

Designer to choose colors to be used in the design.

```html
<!DOCTYPE html>
<html lang="en">
<head>
<meta charset="utf-8">
<title>KV Holdings — Business Card</title>
<link href="https://fonts.googleapis.com/css2?family=Montserrat:wght@400;500;700&display=swap" rel="stylesheet">
<style>
  :root {
    --stage: #1c1c1c;
    --card-dark: #111111;
    --card-light: #ffffff;
    --brand-red: #b80c3c;
    --ink: #1a1a1a;
    --ink-soft: #444444;
    --on-dark: #f2f2f2;
    --on-dark-muted: #a9a9a9;
  }
  * { box-sizing: border-box; margin: 0; padding: 0; }
  html, body { width: 1200px; height: 1015px; overflow: hidden; }
  body {
    background: var(--stage);
    font-family: "Montserrat", Arial, sans-serif;
    display: flex; flex-direction: column; align-items: center; justify-content: center;
    gap: 56px;
  }
  .card {
    width: 640px; height: 366px; position: relative;
    box-shadow: 0 10px 30px rgba(0,0,0,.5);
  }

  /* Front (dark) */
  .card--front { background: var(--card-dark); color: var(--on-dark); }
  .front__est {
    position: absolute; left: 300px; top: 78px;
    font-size: 13px; font-weight: 500; letter-spacing: 4px; color: var(--on-dark);
  }
  .front__wordmark {
    position: absolute; left: 150px; top: 100px;
    font-size: 54px; font-weight: 700; color: var(--brand-red); letter-spacing: 1px;
  }
  .front__rule {
    position: absolute; height: 2px; background: var(--brand-red);
  }
  .front__rule--short { left: 170px; width: 310px; top: 178px; }
  .front__rule--long { left: 60px; width: 520px; top: 238px; }
  .brand-row {
    position: absolute; left: 60px; right: 60px; top: 262px;
    display: flex; justify-content: space-between; align-items: center;
  }
  .brand {
    display: flex; align-items: center; gap: 8px;
    font-size: 18px; font-weight: 700; color: var(--on-dark-muted);
  }
  .brand__dot { width: 12px; height: 12px; background: var(--on-dark-muted); }
  .brand__dot--round { border-radius: 50%; }

  /* Back (light) */
  .card--back { background: var(--card-light); color: var(--ink); }
  .back__logo {
    position: absolute; left: 40px; top: 118px; width: 250px; text-align: center;
  }
  .back__wordmark { font-size: 40px; font-weight: 700; color: var(--brand-red); line-height: 1.1; }
  .back__logo-rule { height: 2px; background: var(--brand-red); margin: 10px 20px 8px; }
  .back__est { font-size: 13px; font-weight: 500; letter-spacing: 4px; color: var(--ink); }
  .back__divider {
    position: absolute; left: 312px; top: 70px; width: 1.5px; height: 180px; background: var(--brand-red);
  }
  .contact { position: absolute; left: 340px; top: 70px; }
  .contact__name { font-size: 22px; font-weight: 500; color: var(--brand-red); letter-spacing: .5px; }
  .contact__title { font-size: 15px; color: var(--ink); margin-bottom: 16px; }
  .contact__list { list-style: none; }
  .contact__item {
    display: flex; align-items: center; gap: 10px;
    font-size: 14px; color: var(--ink); line-height: 25px;
  }
  .contact__icon { width: 15px; height: 15px; flex: none; }
  .back__rule {
    position: absolute; left: 40px; right: 40px; top: 282px; height: 2px; background: var(--brand-red);
  }
  .locations {
    position: absolute; left: 0; right: 0; top: 300px;
    display: flex; justify-content: center; align-items: center; gap: 8px;
    font-size: 16px; color: var(--ink);
  }
  .locations__sep { color: var(--brand-red); }
  .locations__pin { width: 14px; height: 18px; }
</style>
</head>
<body>

  <section class="card card--front" aria-label="Card front">
    <p class="front__est">EST. 1971</p>
    <p class="front__wordmark">KV Holdings</p>
    <div class="front__rule front__rule--short"></div>
    <div class="front__rule front__rule--long"></div>
    <div class="brand-row">
      <span class="brand"><span class="brand__dot"></span>Aralia</span>
      <span class="brand"><span class="brand__dot"></span>Strata</span>
      <span class="brand"><span class="brand__dot brand__dot--round"></span>Raincove</span>
      <span class="brand"><span class="brand__dot"></span>Urbanset</span>
    </div>
  </section>

  <section class="card card--back" aria-label="Card back">
    <div class="back__logo">
      <p class="back__wordmark">KV Holdings</p>
      <div class="back__logo-rule"></div>
      <p class="back__est">EST. 1971</p>
    </div>
    <div class="back__divider"></div>
    <div class="contact">
      <p class="contact__name">MARCO BELLANDI</p>
      <p class="contact__title">B.Eng (Civil)</p>
      <ul class="contact__list">
        <li class="contact__item">
          <svg class="contact__icon" viewBox="0 0 16 16"><path d="M3 1.5l3 3-1.6 1.6a9 9 0 005.5 5.5L11.5 10l3 3-2 2C6.5 15 1 9.5 1 3.5z" fill="var(--brand-red)"/></svg>
          0400 123 456
        </li>
        <li class="contact__item">
          <svg class="contact__icon" viewBox="0 0 16 16"><rect x="4" y="1" width="8" height="14" rx="1.5" fill="none" stroke="var(--brand-red)" stroke-width="1.6"/><circle cx="8" cy="12.5" r="0.9" fill="var(--brand-red)"/></svg>
          1300 000 123
        </li>
        <li class="contact__item">
          <svg class="contact__icon" viewBox="0 0 16 16"><rect x="1" y="3" width="14" height="10" fill="var(--brand-red)"/><path d="M1 3l7 6 7-6" fill="none" stroke="#fff" stroke-width="1.3"/></svg>
          marco@kvholdings.com.au
        </li>
        <li class="contact__item">
          <svg class="contact__icon" viewBox="0 0 16 16"><g fill="none" stroke="var(--brand-red)" stroke-width="1.4"><circle cx="8" cy="8" r="6.5"/><ellipse cx="8" cy="8" rx="3" ry="6.5"/><path d="M1.5 8h13M2.5 4.8h11M2.5 11.2h11"/></g></svg>
          www.kvholdings.com.au
        </li>
      </ul>
    </div>
    <div class="back__rule"></div>
    <p class="locations">
      <svg class="locations__pin" viewBox="0 0 14 18"><path d="M7 0a7 7 0 00-7 7c0 5 7 11 7 11s7-6 7-11a7 7 0 00-7-7z" fill="var(--brand-red)"/><circle cx="7" cy="7" r="2.6" fill="#fff"/></svg>
      Adelaide <span class="locations__sep">|</span> Brisbane <span class="locations__sep">|</span> Melbourne <span class="locations__sep">|</span> Perth <span class="locations__sep">|</span> Sydney
    </p>
  </section>

</body>
</html>
```